Kitchen and cabinets Landing Page design

Hi there
Web Design Task Outline
• Create a Web Design
• Uncoded webpage layout design
• Single Page - Just Homepage Layout
Task Description
* While we need to update our website, we are actually looking at working with a web designer long-term, which will include quite regular design work. So even though this is a small job, we’d love you to respond, as if you do a good job on this one, we would love to continue working with you on a more regular basis.
Please find below all the information for the design of our new website.
The current Web site is www.marrowbank.com.au – don’t laugh!!!
Site Basics:
The site will be the landing page and online home of our kitchen renovation business. We also do vanities, bedroom robes and general cabinetery for the house and office.
Target audience:
? Predominantly home renovation seekers, families (females – decision maker) and builders.
? Most of our business comes from referrals and recommendations, but the site needs to be updated to improve our on line image
General feeling to be conveyed:
Update our old, tired 80’s site (fresh, modern and vital)
Must portray contemporary and up to date attitude - eye-catching / attention grabbing
But not too expensive looking as to alienate people who may think we look too expensive
Landing Page:
Happy to look at your creativity, but must contain a capturing image, contact details (phone), testimonials
Potential Nav Links =
Home
Photo Gallery
Contact Us
Testimonial
Vanities
Entertainment Units
Colours:
Our business has little to do with wood now so the timber look is superseded. We are open to your creative suggestions. We need all marketing media to be consistent and the website can start this process. Our logo is really weak and dated as well. At present we have a green and blue business card with capital QP logo (hmmm), but we’re generally thinking something that represents the home and kitchen
Layout: Open to your creativity
* Samples of Other Good (Similar) Sites We Like:
www.hobplexa.com.au
www.vorny.com.au
www.primacabinetry.com.au/
www.lunafitouts.com.au
www.thejoinerycourt.com.au
Header Text =
Feel free to submit something from your own creative ideas.
Header Image/photo Ideas:
As the site is about kitchen and house hold cabinets, feel free to use an image to reflect that. We are generally thinking to have one main image that is quite eye-catching and attention grabbing. We can supply photos from jobs we have done later.
* Notes:
1. Do not feel completely bound to these ideas. Feel free to convey the basic idea however your creativity desires.
Thanks a lot and look forward to receiving your first design!
Cheers
Gordon
Updates
sorry people - forgot to mention our best selling point!
we were established in 1980, so have been going for 30 years. This is a strong selling point.
We use "30 years of excellence" as a tag.
there are numerous ways of using est. 1980, ie gold label, starburst etc. Go for it.
thanks
Gordon
Hi Designers, My apologies for the delay in responding to your designs. I have been working on other business and have not had a chance to look at them thoroughly. I plan to focus on them today and will provide feedback. Thank you for your understanding.
Reason: Today was the first chance I've had to look at designs. Will be actively providing feedback over next fews day. Am looking to make some changes to the a few of the designs received. Thanks everyone for you patience.

```html
<!DOCTYPE html>
<html lang="en">
<head>
<meta charset="utf-8">
<title>Marrowbank Cabinets &amp; Furniture</title>
<link href="https://fonts.googleapis.com/css2?family=Arimo:wght@400;700&family=Fredoka:wght@600&family=Didact+Gothic&display=swap" rel="stylesheet">
<style>
:root{
  --tan:#c8974f;
  --tan-light:#d4a65f;
  --gold:#c3873a;
  --panel:#f4f4f4;
  --ink:#111;
  --white:#fff;
  --line:#d8d8d8;
}
*{box-sizing:border-box;margin:0;padding:0}
html,body{width:1200px;height:904px;overflow:hidden;background:var(--tan)}
.stage{position:absolute;left:0;top:0;width:1280px;height:964px;transform:scale(.9375);transform-origin:0 0;font-family:"Arimo",Arial,sans-serif;color:var(--ink)}
.abs{position:absolute}
.frame{left:140px;top:22px;width:998px;height:846px;background:var(--tan-light);border-radius:14px}
.panel{left:160px;top:40px;width:958px;height:812px;background:linear-gradient(#f7f7f7,#efefef);border-radius:12px;box-shadow:0 1px 4px rgba(0,0,0,.5)}
.brand{left:184px;top:55px;width:192px;height:126px;border-radius:50%;background:#e9e6e1;border:2px solid #b7b0a6;display:flex;align-items:center;justify-content:center;gap:8px;font-family:"Fredoka",sans-serif;font-weight:600;font-size:24px;color:var(--gold)}
.brand i{width:12px;height:12px;background:var(--gold);border-radius:50%;display:block}
.tagline{left:414px;top:92px;font-family:"Fredoka",sans-serif;font-weight:600;font-size:26px;color:var(--gold);line-height:31px}
.tagline span{display:block}
.tagline .second{padding-left:22px}
.tagline b{font-size:14px;font-weight:600;margin-right:6px;vertical-align:3px}
.contact{left:829px;top:82px;font-size:16px;line-height:18px}
.hero{left:180px;top:193px;width:920px;height:437px;border-radius:10px 10px 0 0;overflow:hidden;background:linear-gradient(180deg,#d9d2c8 0%,#e8e3dc 40%,#f1ede7 70%,#a45a3a 100%)}
.thumbs{left:180px;top:241px;width:134px;height:319px;background:#000;border-radius:12px}
.thumb{left:193px;width:106px;height:85px;border-radius:10px;border:1px solid #ccc}
.t1{top:261px;background:linear-gradient(#c7b8a6,#8a3c22)}
.t2{top:358px;background:linear-gradient(#c0a990,#5d4a3a)}
.t3{top:455px;background:linear-gradient(#dcd6cd,#4b3a30)}
.quote{left:687px;top:390px;width:413px;height:213px;background:rgba(255,255,255,.55);border-radius:12px 0 0 12px;font-family:"Didact Gothic",sans-serif;font-style:italic;color:#222;padding:10px 12px 0 20px}
.quote p{font-size:20px;line-height:21.5px}
.quote .who{margin-top:10px;font-size:19px}
.more{left:1011px;top:589px;font-family:"Didact Gothic",sans-serif;font-size:13px;color:#111}
.mission-shelf{left:180px;top:612px;width:920px;height:46px;background:#f3f3f3;border-radius:14px 14px 0 0}
.mission{left:188px;top:620px;width:904px;height:33px;border-radius:12px;background:linear-gradient(#e6b679,#c68a43);border:1px solid #b07734;color:var(--white);font-size:15px;text-align:center;line-height:33px;text-shadow:0 1px 1px rgba(0,0,0,.4)}
.card{top:680px;height:147px;background:linear-gradient(#f0f0f0,#fff);border:1px solid var(--line);border-radius:10px}
.services{left:179px;width:311px}
.service{position:absolute;left:14px;display:flex;gap:8px;font-size:11px;line-height:13.5px}
.service .pic{width:92px;height:58px;border-radius:6px;border:2px solid #fff;box-shadow:0 0 0 1px #aaa;flex:none}
.featured{left:507px;width:265px}
.featured .pic{position:absolute;left:18px;top:9px;width:230px;height:106px;border-radius:6px;border:2px solid #fff;box-shadow:0 0 0 1px #999;background:linear-gradient(90deg,#5a4a40,#2e2926 50%,#6d5e52)}
.featured p{position:absolute;left:16px;top:125px;font-size:12.5px}
.enquiry{left:789px;width:311px}
.enquiry h2{position:absolute;left:15px;top:10px;font-weight:400;font-size:15px}
.enquiry .intro{position:absolute;left:16px;top:34px;font-size:10.5px;line-height:18px;width:290px}
.enquiry .intro b{font-size:14px;margin-left:4px}
.field{position:absolute;left:12px;width:192px;height:21px;border:1px solid #bbb;border-radius:11px;background:#fff;font-size:10px;padding:3px 9px}
.submit{position:absolute;left:211px;top:110px;width:83px;height:22px;border-radius:11px;background:linear-gradient(#e1b27a,#c0843f);border:1px solid #a66e2e;color:var(--white);font-family:"Fredoka",sans-serif;font-size:14px;text-align:center;line-height:20px;text-shadow:0 1px 1px rgba(0,0,0,.4)}
.slogan{left:168px;top:885px;width:944px;height:32px;border-radius:14px;background:linear-gradient(#fff,#e4e4e4);border:1px solid #999;text-align:center;line-height:32px;font-family:"Didact Gothic",sans-serif;font-size:15.5px}
.copyright{left:0;top:934px;width:1280px;text-align:center;color:var(--white);font-weight:700;font-size:12px}
</style>
</head>
<body>
<div class="stage">
  <div class="abs frame"></div>
  <div class="abs panel"></div>

  <div class="abs brand"><i></i>Marrowbank</div>

  <div class="abs tagline">
    <span><b>&rarr;</b>Established 1980</span>
    <span class="second"><b>&rarr;</b>30 years of experience</span>
  </div>

  <div class="abs contact">
    <b>Tel:</b> 039841-616 | <b>Fax:</b> 0398416170<br>
    <b>Address:</b>Unit 5, 418<br>
    Hollis Road, Carrow Vale<br>
    Email:gordon@marrowbank.com.au
  </div>

  <div class="abs hero" role="img" aria-label="Bright white kitchen with island bench, stone benchtops and timber floor"></div>
  <div class="abs thumbs"></div>
  <div class="abs thumb t1" role="img" aria-label="Open plan kitchen with timber floor"></div>
  <div class="abs thumb t2" role="img" aria-label="Built-in entertainment unit"></div>
  <div class="abs thumb t3" role="img" aria-label="Kitchen island with downlights"></div>

  <blockquote class="abs quote">
    <p>&ldquo; The advice we received from everyone at Marrowbank was sound, considered and sensitive. We appreciated the staff being here at the time and date arranged and all were a pleasure to deal with. Apart from being extremely competent. &rdquo;</p>
    <p class="who">Ruth and Alan Penfold, Elm Rise</p>
  </blockquote>
  <div class="abs more">View More...</div>

  <div class="abs mission-shelf"></div>
  <div class="abs mission">OUR MISSION: To produce excellent quality cabinetry every time! and a high level of personal workmanship....</div>

  <section class="abs card services">
    <div class="service" style="top:10px">
      <div class="pic" role="img" aria-label="Kitchen with island bench" style="background:linear-gradient(#cbbcaa,#8a3c22)"></div>
      <p>We custom design, build and install quality cabinets, kitchens, bathrooms, laundries, theatre entertainments units, studies and wardrobes</p>
    </div>
    <div class="service" style="top:78px">
      <div class="pic" role="img" aria-label="Study with built-in desk and shelving" style="background:linear-gradient(#d9d0bf,#9c8a70)"></div>
      <p>We custom design, build and install quality cabinets, kitchens, bathrooms, laundries, theatre entertainments units, studies and wardrobes</p>
    </div>
  </section>

  <section class="abs card featured">
    <div class="pic" role="img" aria-label="Living room with fireplace and built-in bookshelves"></div>
    <p>As featured in Living Spaces, June 2011"</p>
  </section>

  <section class="abs card enquiry">
    <h2>Enquiry Now</h2>
    <p class="intro">For an obligation FREE consultation and quote use our online enquiry form or call us now on <b>039841 616</b></p>
    <div class="field" style="top:77px">Name:</div>
    <div class="field" style="top:110px">Email:</div>
    <div class="submit">Submit</div>
  </section>

  <div class="abs slogan">" We are proud of our innovative designs, superior products and outstanding service sought after by the discerning customer"</div>
  <div class="abs copyright">Copyright &copy; 2011 Marrowbank.Com</div>
</div>
</body>
</html>
```